7th Annual Falcon Invitational Flyer

Looking to design an updated eye catching flyer maybe with someone movement, sound, and color. Below is an attachment of the flyer I have used in the past. I need to add color, sound, and movement to the flyer. This is an advertisement for youth folk style wrestling. You may contact me directly at 252-381-4926 if you need additional information. I really like the colors music and movement in the video below.
https://www.vidmarlo.com/watch?v=qT4kLmPzw8e

Target Market(s)

Youth Wrestling

Font styles to use
Serif

Colors
EB3D1F
EC4F4E
F09395
F8D3D4
FCEDEE

Requirements
Must have
• All information included on flyer.
Nice to have
• Color, sound, and movement

```html
<!DOCTYPE html>
<html lang="en">
<head>
<meta charset="utf-8">
<title>7th Annual Falcon Invitational</title>
<link rel="stylesheet" href="https://fonts.googleapis.com/css2?family=Open+Sans:wght@400;600;700&display=swap">
<style>
  :root {
    --flame: #EB3D1F;
    --coral: #EC4F4E;
    --rose: #F09395;
    --blush: #F8D3D4;
    --mist: #FCEDEE;
    --ink: #2e2a2a;
  }
  * { box-sizing: border-box; margin: 0; padding: 0; }
  html, body { width: 848px; height: 1200px; overflow: hidden; background: var(--blush); }
  .flyer {
    position: relative;
    width: 848px;
    height: 1200px;
    overflow: hidden;
    background: var(--blush);
    font-family: "Open Sans", Arial, sans-serif;
    color: var(--ink);
  }
  .backdrop { position: absolute; inset: 0; }
  .crest-backdrop {
    position: absolute;
    left: 175px; top: 190px;
    width: 500px; height: 700px;
    border-radius: 250px 250px 40px 40px;
    background: radial-gradient(ellipse at 50% 40%, rgba(200,150,150,0.28), rgba(200,150,150,0.08) 70%, transparent);
  }
  .brand-mark {
    position: absolute;
    right: 40px; top: 42px;
    display: flex; align-items: center; gap: 10px;
    font-weight: 700; font-size: 17px; color: var(--flame);
  }
  .brand-mark .dot {
    width: 40px; height: 40px; border-radius: 50%; background: var(--coral);
  }
  .title {
    position: absolute; left: 28px; top: 30px;
    font-size: 37px; font-weight: 600; color: var(--flame); letter-spacing: 0.2px;
  }
  .info-row {
    position: absolute; left: 28px;
    display: flex; align-items: center; gap: 20px;
    font-size: 18.5px; line-height: 30px;
  }
  .info-row svg { flex: none; width: 36px; height: 36px; }
  .info-row.date { top: 97px; }
  .info-row.venue { top: 156px; }
  .info-row.times { top: 236px; }
  .info-row.times svg { align-self: center; }
  .details {
    position: absolute; left: 28px; top: 321px;
    list-style: none; font-size: 19.5px; line-height: 33.6px;
  }
  .panel {
    position: absolute; top: 556px;
    width: 382px; height: 612px;
    border-radius: 12px;
    background: rgba(252,237,238,0.92);
    padding: 14px 18px;
  }
  .panel.boys { left: 28px; }
  .panel.girls { left: 436px; }
  .panel h2 {
    font-size: 28px; font-weight: 700; color: var(--flame);
    margin-bottom: 6px; word-spacing: 4px;
  }
  .panel p { font-size: 16.6px; line-height: 36.6px; }
</style>
</head>
<body>
<main class="flyer">
  <svg class="backdrop" width="848" height="1200" viewBox="0 0 848 1200" aria-hidden="true">
    <polygon points="690,0 790,0 0,1000 0,860" fill="var(--rose)" opacity="0.75"/>
    <polygon points="848,70 848,210 690,345 848,480 848,620 600,345" fill="var(--coral)" opacity="0.55"/>
    <polygon points="0,1070 0,1200 90,1200 210,1050" fill="var(--coral)" opacity="0.6"/>
    <polygon points="350,1200 420,1160 480,1200" fill="var(--rose)" opacity="0.6"/>
  </svg>
  <div class="crest-backdrop" role="img" aria-label="Faint falcon crest emblem in the background"></div>

  <div class="brand-mark"><span class="dot"></span>Falcon Invitational</div>

  <h1 class="title">7th Annual Falcon Invitational</h1>

  <div class="info-row date">
    <svg viewBox="0 0 36 36" fill="none" stroke="var(--flame)" stroke-width="2">
      <rect x="4" y="7" width="28" height="25" rx="3"/>
      <line x1="4" y1="14" x2="32" y2="14"/>
      <line x1="11" y1="3" x2="11" y2="10"/><line x1="25" y1="3" x2="25" y2="10"/>
      <rect x="9" y="18" width="4" height="3"/><rect x="16" y="18" width="4" height="3"/><rect x="23" y="18" width="4" height="3"/>
      <rect x="9" y="25" width="4" height="3"/><rect x="16" y="25" width="4" height="3"/><rect x="23" y="25" width="4" height="3"/>
    </svg>
    <span>Saturday, January 25, 2025</span>
  </div>

  <div class="info-row venue">
    <svg viewBox="0 0 36 36" fill="none" stroke="var(--flame)" stroke-width="2.4">
      <path d="M18 33 C10 23 7 18 7 13 A11 11 0 0 1 29 13 C29 18 26 23 18 33 Z"/>
      <circle cx="18" cy="13" r="4"/>
    </svg>
    <span>Riverside Events Hall<br>418 Harbor Blvd SW Riverside, NC 27901</span>
  </div>

  <div class="info-row times">
    <svg viewBox="0 0 36 36" fill="none" stroke="var(--flame)" stroke-width="2.2">
      <circle cx="18" cy="18" r="14"/>
      <polyline points="18,9 18,18 24,22"/>
    </svg>
    <span>4U, 6U, 8U, 10U – Wrestling Starts at 8:30 am<br>12U, Middle School, &amp; High School – Wrestling Starts at 1:00 pm</span>
  </div>

  <ul class="details">
    <li>Register @ www.matbracket.com</li>
    <li>Early Registration $30.00 Deadline is January 19, 2025 at 11:59PM</li>
    <li>Regular Registration $40.00 Deadline is January 22, 2025 at 11:59PM</li>
    <li>Late Registration $50.00 Deadline is January 24, 2025 at 5:00PM</li>
    <li>Registration is limited to the first 500 wrestlers</li>
    <li>Non-CYWL Card Holders will pay an additional $5.00 at weigh-ins.</li>
  </ul>

  <section class="panel boys">
    <h2>Boys Divisions</h2>
    <p>4 &amp; Under - 30, 40, 50, HWT<br>
    6 &amp; Under - 36, 40, 44, 48, 52, 56, 60, HWT<br>
    8 &amp; Under - 40, 44, 48, 52, 56, 60, 64, 68,<br>72, 76, 80, 84, 88, 92, HWT<br>
    10 &amp; Under - 52, 56, 60, 64, 68, 72, 76, 80,<br>84, 88, 92, 96, 100, 110, HWT<br>
    12 &amp; Under - 64, 68, 72, 76, 80, 84, 88, 92,<br>96, 100, 105, 110, 115, 120, 130, 140, 160,<br>HWT<br>
    Middle School - 72, 76, 80, 88, 92, 96, 100,<br>105, 110, 115, 120, 130, 140, 160, 210,<br>HWT<br>
    High School - 106, 113, 120, 126, 132,<br>138, 144, 150, 157, 165, 175, 190, 215,<br>HWT</p>
  </section>

  <section class="panel girls">
    <h2>Girls Divisions</h2>
    <p>K-5 - 36, 40, 44, 48, 52, 56, 60, 64, 68, 72,<br>76, 80, 84, 88, 92, 96, 100, 110, 120,HWT<br>
    Middle School – 72, 76, 83, 90, 98, 106,<br>113, 120, 126, 132, 138, 145, 152, 160,<br>170, 182, 190, 220, HWT<br>
    Women’s High School 100, 107, 114, 120,<br>126, 132, 145, 152, 165, 185, HWT<br>
    *Age is based upon wrestler’s age as of<br>December 31, 2024.<br>
    Tournament director has the right to<br>combine weight classes if deemed<br>necessary.</p>
  </section>
</main>
</body>
</html>
```